Granite Ridge Holdings

I have a real estate investment business.

** I need editable vector files of the final design.

Industry/Entity Type

Real Estate

Contact Information for Business Card

I would like the card to be clear and direct with the company name and contact info. I would prefer not to have a design that is too busy (i.e., with excessive detail) in the business card.

Font styles to use
Sans Serif

Requirements
Must have
• My card must have the following information listed below:
• Company name: Grainite Ridge Holdings LLC
• My name: Daniel Vorsley
• Phone number: (555) 218-9067
• Email address: dtvorsley@mailbox-example.net
• Keywords: “Real Estate Investments”
Nice to have
• I would like to have a design that resembles the characteristics/uses of obsidian stone which resembles something related to strength and resilience. Perhaps something with sharp, sleek color transitions as well.

```html
<!DOCTYPE html>
<html lang="en">
<head>
<meta charset="utf-8">
<title>Grainite Ridge Holdings LLC – Business Card</title>
<link rel="stylesheet" href="https://fonts.googleapis.com/css2?family=Alegreya+Sans:wght@400;500&family=Alegreya+Sans+SC:wght@400;500&display=swap">
<style>
  :root {
    --backdrop: #e2e2e2;
    --card: #ffffff;
    --ink: #111111;
    --slate: #4b4b4d;
    --charcoal: #2a2a2b;
    --obsidian: #000000;
    --light-text: #ffffff;
  }
  * { margin: 0; padding: 0; box-sizing: border-box; }
  html, body {
    width: 1200px;
    height: 1200px;
    overflow: hidden;
    background: var(--backdrop);
  }
  .canvas {
    position: relative;
    width: 1200px;
    height: 1200px;
    display: flex;
    align-items: center;
    justify-content: center;
  }
  .business-card {
    position: relative;
    width: 1100px;
    height: 630px;
    background: var(--card);
    overflow: hidden;
  }
  .brand {
    position: absolute;
    top: 0;
    left: 0;
    width: 100%;
    height: 291px;
    display: flex;
    align-items: center;
    justify-content: center;
    gap: 26px;
    padding-top: 20px;
  }
  .brand-mark {
    width: 40px;
    height: 40px;
    background: var(--ink);
  }
  .brand-name {
    font-family: "Alegreya Sans SC", sans-serif;
    font-weight: 500;
    font-size: 50px;
    color: var(--ink);
    letter-spacing: 0.5px;
  }
  .contact-band {
    position: absolute;
    top: 291px;
    left: 0;
    width: 100%;
    height: 218px;
    display: flex;
  }
  .band-accent {
    width: 140px;
    background: var(--slate);
  }
  .band-name {
    width: 410px;
    background: var(--charcoal);
    display: flex;
    align-items: center;
    justify-content: center;
  }
  .person-name {
    font-family: "Alegreya Sans", sans-serif;
    font-weight: 400;
    font-size: 40px;
    color: var(--light-text);
    padding-top: 14px;
  }
  .band-details {
    flex: 1;
    background: var(--obsidian);
    display: flex;
    flex-direction: column;
    justify-content: center;
    gap: 38px;
    padding-left: 43px;
  }
  .detail-row {
    display: flex;
    align-items: center;
    gap: 37px;
    color: var(--light-text);
  }
  .detail-icon {
    width: 40px;
    height: 40px;
    flex: none;
  }
  .phone-number {
    font-family: "Alegreya Sans", sans-serif;
    font-size: 28px;
  }
  .email-address {
    font-family: "Alegreya Sans SC", sans-serif;
    font-size: 23px;
    letter-spacing: 0.6px;
  }
  .tagline {
    position: absolute;
    top: 509px;
    left: 0;
    width: 100%;
    height: 121px;
    display: flex;
    align-items: center;
    justify-content: center;
    font-family: "Alegreya Sans SC", sans-serif;
    font-size: 31px;
    color: var(--ink);
    letter-spacing: 1px;
    padding-bottom: 6px;
  }
</style>
</head>
<body>
<main class="canvas">
  <section class="business-card">
    <header class="brand">
      <span class="brand-mark" aria-hidden="true"></span>
      <h1 class="brand-name">Grainite Ridge Holdings LLC</h1>
    </header>

    <div class="contact-band">
      <div class="band-accent"></div>
      <div class="band-name">
        <p class="person-name">Daniel Vorsley</p>
      </div>
      <div class="band-details">
        <div class="detail-row">
          <svg class="detail-icon" viewBox="0 0 24 24" aria-hidden="true">
            <path fill="#ffffff" d="M6.6 10.8c1.4 2.8 3.8 5.1 6.6 6.6l2.2-2.2c.3-.3.7-.4 1-.2 1.1.4 2.3.6 3.6.6.6 0 1 .4 1 1V20c0 .6-.4 1-1 1C10.6 21 3 13.4 3 4c0-.6.4-1 1-1h3.5c.6 0 1 .4 1 1 0 1.3.2 2.5.6 3.6.1.3 0 .7-.2 1l-2.3 2.2z"/>
          </svg>
          <span class="phone-number">(555) 218-9067</span>
        </div>
        <div class="detail-row">
          <svg class="detail-icon" viewBox="0 0 40 40" aria-hidden="true">
            <rect x="2" y="9" width="36" height="23" fill="none" stroke="#ffffff" stroke-width="2"/>
            <polyline points="2,9 20,23 38,9" fill="none" stroke="#ffffff" stroke-width="2"/>
            <polyline points="2,32 16,20 M24,20 38,32" fill="none" stroke="#ffffff" stroke-width="2"/>
            <line x1="24" y1="20" x2="38" y2="32" stroke="#ffffff" stroke-width="2"/>
          </svg>
          <span class="email-address">dtvorsley@mailbox-example.net</span>
        </div>
      </div>
    </div>

    <p class="tagline">Real Estate Investments</p>
  </section>
</main>
</body>
</html>
```